Alternative Health Practice - Website redesign

With regard to the welcome image, stock photos can't show the faces of other people. And please don't submit a design for a one-page website.
Hello, I am redesigning a website and need some help from a professional.
The old website is here: peter-lindqvist.net (pls note I don't want to reuse the welcome photo from the old site). Much of the written content will remain the same, so note that I also need a page layout/text colour etc that works for text heavy pages: ie www.peter-lindqvist.net/somatic-articles and www.peter-lindqvist.net/client-reviews
My effort at redesigning is underway here: https://pjlindqvist.sitebuilderhost.net/my-site-7
The original sitebuilder template is this one: https://www.sitebuilderhost.net/website-template/view/html/4917?originUrl=https%3A%2F%2Fwww.sitebuilderhost.net%2Fwebsite%2Ftemplates%2Fhtml%2Fhealth-wellness&tpClick=view_button&esi=8a41c27d-03e9-4c6b-b1f2-9d5e02a7c4f3
I'm pretty happy with the colour palette. My name Peter Joseph Lindqvist is now the "brand" without Rooted Stillness subtitle. Regarding the Welcome section, if you are going to use my photos, it probably needs to be those two that are already there. If you want to put a stock photo there instead, that's fine.
If you want to propose something quite different to my design, I'm happy to receive design files in Photoshop or whatever and then subsequently replicate on Sitebuilder. Up to you.
Mostly women, some men ages 28-60.

```html
<!DOCTYPE html>
<html lang="en">
<head>
<meta charset="utf-8">
<title>Peter Joseph Lindqvist</title>
<link href="https://fonts.googleapis.com/css2?family=Figtree:wght@300;400;500;600;700&display=swap" rel="stylesheet">
<style>
:root{
  --dark:#3a3d33;
  --dark-2:#3e4137;
  --light:#e1e3dd;
  --cream:#e6e7e1;
  --ink:#35382f;
  --muted:#5b5e55;
  --gold:#b0842e;
  --white:#ffffff;
}
*{margin:0;padding:0;box-sizing:border-box}
html,body{width:1200px;height:4060px;overflow:hidden}
body{font-family:"Figtree",sans-serif;background:var(--dark);color:var(--white);position:relative}
.abs{position:absolute}
section,header,footer{position:absolute;left:0;width:1200px;overflow:hidden}

/* header */
.site-header{top:0;height:98px;background:var(--dark-2)}
.brand{display:flex;align-items:center;gap:12px;left:48px;top:20px}
.brand-dot{width:56px;height:56px;border-radius:50%;background:var(--gold)}
.brand-name{font-weight:700;font-size:20px;line-height:21px;letter-spacing:.3px;color:var(--white)}
.nav{top:40px;left:380px;display:flex;gap:0;font-size:16px;font-weight:400}
.nav span{position:absolute;white-space:nowrap}
.btn-pill{background:var(--cream);color:var(--ink);border-radius:30px;display:flex;align-items:center;justify-content:center;font-weight:500}
.nav-cta{left:993px;top:32px;width:153px;height:39px;font-size:15px}

/* hero */
.hero{top:98px;height:604px}
.hero-photo{left:0;top:0;width:1200px;height:604px;background:
  radial-gradient(ellipse 420px 300px at 880px 330px,#b59a82 0%,#8a7a66 35%,transparent 70%),
  radial-gradient(ellipse 320px 420px at 130px 200px,#5f6e4f 0%,transparent 70%),
  linear-gradient(120deg,#56604a 0%,#6d745e 45%,#7a7560 70%,#5a5c4c 100%)}
.hero-shade{left:0;top:0;width:1200px;height:604px;background:rgba(58,61,51,.35)}
.hero-title{left:0;top:166px;width:1200px;text-align:center;font-size:54px;font-weight:600;line-height:54px}
.hero-arrow{left:515px;top:298px}
.hero-cta{left:495px;top:359px;width:211px;height:46px;font-size:22px}

/* about */
.about{top:702px;height:804px;background:var(--dark)}
.section-title{font-weight:600;font-size:44px;line-height:48px}
.about-title{left:128px;top:70px}
.about-sub{left:128px;top:118px;font-size:25px;font-weight:500}
.about-photo{left:282px;top:198px;width:297px;height:425px;border-radius:8px;background:
  radial-gradient(ellipse 120px 150px at 150px 180px,#a47a5f 0%,transparent 75%),
  linear-gradient(160deg,#6f8a4c 0%,#4d5f3a 50%,#5b6a45 100%)}
.about-text{left:632px;top:223px;width:448px;font-size:15px;line-height:21px;font-weight:400}
.about-text p{margin-bottom:21px}
.btn-outline{border:1.5px solid var(--white);border-radius:30px;display:flex;align-items:center;justify-content:center;font-size:17px;font-weight:500;color:var(--white)}
.about-more{left:516px;top:689px;width:170px;height:51px}

/* articles */
.articles{top:1506px;height:749px;background:var(--light);color:var(--ink)}
.articles-title{left:0;top:74px;width:1200px;text-align:center;font-size:41px}
.card{top:191px;width:298px}
.card-img{width:298px;height:217px}
.card-title{margin-top:30px;font-size:22px;line-height:25px;font-weight:600;min-height:50px}
.card-text{margin-top:20px;font-size:14.5px;line-height:21px;color:var(--muted);font-weight:400}
.card-link{margin-top:22px;font-size:16px;font-weight:600;text-decoration:underline;display:block}
.chev{width:24px;height:30px}

/* energy */
.energy{top:2255px;height:647px;background:var(--dark)}
.energy-title{left:127px;top:124px}
.energy-text{left:131px;top:197px;width:426px;font-size:15px;line-height:21px}
.energy-text p{margin-bottom:21px}
.energy-more{left:131px;top:489px;width:171px;height:51px}
.energy-img-back{left:617px;top:82px;width:247px;height:358px;border-radius:10px;background:linear-gradient(180deg,#b9b8ad 0%,#8f8f80 40%,#4a4a5a 75%,#3b3a48 100%)}
.energy-img-front{left:814px;top:148px;width:326px;height:355px;border-radius:10px;border:3px solid var(--dark);background:
  radial-gradient(ellipse 120px 90px at 200px 250px,#b68a6c 0%,transparent 75%),
  linear-gradient(170deg,#9b9a8d 0%,#7f7e71 45%,#cbc7bd 100%)}

/* reviews */
.reviews{top:2902px;height:722px;background:var(--light);color:var(--ink)}
.rev-brand{left:0;top:50px;width:1200px;text-align:center;font-size:34px;font-weight:500;color:#6a6d66}
.rev-score{left:0;top:95px;width:1200px;text-align:center;font-size:20px;color:#6a6d66;letter-spacing:1px}
.reviews-title{left:0;top:125px;width:1200px;text-align:center;font-size:41px}
.review{top:250px;width:340px;text-align:center}
.avatar{width:142px;height:142px;border-radius:50%;margin:0 auto}
.review-name{margin-top:20px;font-size:20px;line-height:24px;font-weight:600;min-height:48px}
.review-text{margin-top:12px;font-size:15px;line-height:23px;color:var(--muted)}

/* footer */
.site-footer{top:3624px;height:436px;background:var(--dark-2)}
.foot-brand{left:131px;top:120px}
.foot-col{top:98px}
.foot-col h4{font-size:22px;font-weight:600;margin-bottom:16px}
.foot-col li{list-style:none;font-size:15px;line-height:20px;margin-bottom:15px;display:flex;gap:12px;align-items:flex-start}
.foot-col svg{flex:none;margin-top:2px}
.social-mark{width:14px;height:14px;border-radius:50%;background:var(--white);flex:none;margin-top:3px}
.copyright{left:0;top:374px;width:1200px;text-align:center;font-size:15px}
.deco{pointer-events:none}
</style>
</head>
<body>

<header class="site-header">
  <div class="abs brand">
    <span class="brand-dot"></span>
    <span class="brand-name">PETER JOSEPH<br>LINDQVIST</span>
  </div>
  <nav class="abs nav">
    <span style="left:0">The Practice</span>
    <span style="left:147px">Feedback</span>
    <span style="left:271px">Approach</span>
    <span style="left:397px">About Me</span>
    <span style="left:522px">Contact</span>
  </nav>
  <div class="abs btn-pill nav-cta">Book a Session</div>
</header>

<section class="hero">
  <div class="abs hero-photo" role="img" aria-label="Practitioner's hands resting on a client's head during a calm healing session"></div>
  <div class="abs hero-shade"></div>
  <h1 class="abs hero-title">Welcome to Peter<br>Joseph Lindqvist</h1>
  <svg class="abs hero-arrow" width="170" height="34" viewBox="0 0 170 34" fill="none" stroke="#fff" stroke-width="2.2" stroke-linecap="round" stroke-linejoin="round">
    <path d="M4 14 C30 4 70 8 50 20 C35 30 80 22 160 12"/>
    <path d="M148 2 L162 12 L148 22"/>
  </svg>
  <div class="abs btn-pill hero-cta">Book a Session</div>
</section>

<section class="about">
  <h2 class="abs section-title about-title">About Peter Joseph Lindqvist</h2>
  <div class="abs about-sub">Rooted Stillness® Teacher</div>
  <div class="abs about-photo" role="img" aria-label="Portrait photo of Peter outdoors among greenery"></div>
  <div class="abs about-text">
    <p>Growing up in Scotland I had a strong connection with nature and the outdoors. Playing outside with friends, with bikes, ball sports, and later mountaineering and rock climbing, was what most interested me.</p>
    <p>I studied at Ardmore University and worked in London for a number of years as a civil servant. I subsequently set up a property business and in 2006, relocated to Spain.</p>
    <p>At thirty years of age, I found that my life had become quite compromised. I'd had a chronic low back problem since I was a teenager and was experiencing a lot of anxiety and stress, especially being around other people.</p>
    <p>For the back-pain, I'd tried physiotherapy, acupuncture, various types of chiropractic and massage and had found little lasting change. &nbsp;I was regularly taking painkillers and an orthopaedic surgeon had recommended surgery.</p>
  </div>
  <div class="abs btn-outline about-more">Read More</div>
</section>

<section class="articles">
  <svg class="abs deco" width="1200" height="749" viewBox="0 0 1200 749" fill="none" stroke="#eef0ea" stroke-width="14">
    <path d="M145 0 C120 160 60 260 -20 330"/>
    <path d="M1240 380 C1120 380 1040 470 1060 580 C1080 690 1180 720 1240 700"/>
    <path d="M1240 520 C1150 560 1080 660 1020 760"/>
  </svg>
  <h2 class="abs section-title articles-title">Somatic Healing Articles</h2>
  <svg class="abs chev" style="left:60px;top:285px" viewBox="0 0 24 30" fill="none" stroke="#fff" stroke-width="2.5"><path d="M18 4 L7 15 L18 26"/></svg>
  <svg class="abs chev" style="left:1126px;top:285px" viewBox="0 0 24 30" fill="none" stroke="#fff" stroke-width="2.5"><path d="M6 4 L17 15 L6 26"/></svg>

  <article class="abs card" style="left:118px">
    <div class="card-img" role="img" aria-label="Illustration of a stone-like brain in a misty green landscape" style="background:radial-gradient(ellipse 100px 80px at 150px 110px,#4d5245 0%,transparent 80%),linear-gradient(160deg,#9aa290 0%,#6c7660 60%,#505848 100%)"></div>
    <h3 class="card-title">You are not your mind<br>so who's in control of you?</h3>
    <p class="card-text">The problem is that your mind wants to be in control, full stop. &nbsp;The reason for this stems from a generalisation of the survival threat felt by your infant self....</p>
    <span class="card-link">Read More</span>
  </article>
  <article class="abs card" style="left:453px">
    <div class="card-img" role="img" aria-label="Heart-shaped tree silhouetted against a warm sunset" style="background:radial-gradient(ellipse 140px 70px at 150px 170px,#d49a5a 0%,transparent 80%),linear-gradient(180deg,#3a3242 0%,#6a4a48 55%,#b07a4c 100%)"></div>
    <h3 class="card-title">Forgiveness is good<br>for you</h3>
    <p class="card-text">Forgiveness can be a tricky word to use because it comes laden with religious and moralistic misunderstandings. &nbsp;In our society, somehow we've inherited......</p>
    <span class="card-link">Read More</span>
  </article>
  <article class="abs card" style="left:784px">
    <div class="card-img" role="img" aria-label="Illustration of two women embracing among leaves" style="background:radial-gradient(ellipse 110px 90px at 150px 150px,#d9a04a 0%,transparent 80%),linear-gradient(160deg,#c9cdb8 0%,#8da07a 60%,#5f7352 100%)"></div>
    <h3 class="card-title">Clarity: Self vs. Other</h3>
    <p class="card-text">Ok so let's imagine a simple example where two people agree to meet to do something, could be a work-thing, or a social hang-out, or whatever. ......</p>
    <span class="card-link">Read More</span>
  </article>
</section>

<section class="energy">
  <h2 class="abs section-title energy-title">Energy Healing</h2>
  <div class="abs energy-text">
    <p>An session begins by identifying your intention or wish. &nbsp;You may be facing physical or emotional challenges or seeking healing with another aspect of your life.</p>
    <p>A session typically begins by clarifying your intention or wish. You may be facing physical or emotional challenges or seeking help with another aspect of your life, such as family or relationship problems.</p>
    <p>With your interest in the work clarified, I will assess how energy is flowing in your body and where there are blockages in the physical structure.</p>
  </div>
  <div class="abs btn-outline energy-more">Read More</div>
  <div class="abs energy-img-back" role="img" aria-label="Practitioner working with a client's legs on a treatment table"></div>
  <div class="abs energy-img-front" role="img" aria-label="Practitioner resting a hand on a reclining client's forehead"></div>
</section>

<section class="reviews">
  <svg class="abs deco" width="1200" height="722" viewBox="0 0 1200 722" fill="none" stroke="#eef0ea" stroke-width="14">
    <path d="M-20 20 C80 60 90 200 -20 290"/>
    <path d="M1240 300 C1140 340 1080 480 1100 560 C1110 620 1150 680 1240 700"/>
  </svg>
  <div class="abs rev-brand">Revuo</div>
  <div class="abs rev-score">5.0 ★★★★★</div>
  <h2 class="abs section-title reviews-title">Feedback and Client Reviews</h2>
  <svg class="abs chev" style="left:60px;top:292px" viewBox="0 0 24 30" fill="none" stroke="#fff" stroke-width="2.5"><path d="M18 4 L7 15 L18 26"/></svg>
  <svg class="abs chev" style="left:1126px;top:292px" viewBox="0 0 24 30" fill="none" stroke="#fff" stroke-width="2.5"><path d="M6 4 L17 15 L6 26"/></svg>

  <div class="abs review" style="left:90px">
    <div class="avatar" role="img" aria-label="Client photo" style="background:linear-gradient(160deg,#6f8c5a,#a88268)"></div>
    <h3 class="review-name">Lucía<br>Moreno Vidal</h3>
    <p class="review-text">You have given me a lot of confidence in myself. You are showing me a new way of life. And I've learned that it is possible to handle the physical pain caused by our emotions. I didn't know how to cope with it. &nbsp;Thank you...</p>
  </div>
  <div class="abs review" style="left:429px">
    <div class="avatar" role="img" aria-label="Client photo" style="background:linear-gradient(160deg,#7a7790,#d79ab4)"></div>
    <h3 class="review-name">Greta Halvorsen</h3>
    <p class="review-text">In 20 years as a bodyworker I've never felt something like this... it's so beautiful, so complete. &nbsp;The change I've noticed is that in some way what I knew mentally is now integrated. &nbsp;I feel more connected... I trust more...</p>
  </div>
  <div class="abs review" style="left:768px">
    <div class="avatar" role="img" aria-label="Client photo" style="background:linear-gradient(160deg,#d8a88c,#3d8fc0)"></div>
    <h3 class="review-name">Dale Whitford</h3>
    <p class="review-text">I went to see Peter with 2 separate problems. I had very painful sciatica on one occasion and a painful elbow and shoulder on another. &nbsp;During the sessions I noticed a lot of different sensations. There was a feeling of balancing..</p>
  </div>
</section>

<footer class="site-footer">
  <div class="abs brand foot-brand">
    <span class="brand-dot"></span>
    <span class="brand-name">PETER JOSEPH<br>LINDQVIST</span>
  </div>
  <div class="abs foot-col" style="left:454px">
    <h4>Home</h4>
    <ul><li>The Practice</li><li>Feedback</li><li>Approach</li><li>Contact</li><li>Blog</li></ul>
  </div>
  <div class="abs foot-col" style="left:613px">
    <h4>Contact</h4>
    <ul>
      <li><svg width="18" height="18" viewBox="0 0 24 24" fill="none" stroke="#fff" stroke-width="1.6"><path d="M5 3h4l2 5-2.5 1.5a11 11 0 0 0 6 6L16 13l5 2v4a2 2 0 0 1-2 2A17 17 0 0 1 3 5a2 2 0 0 1 2-2z"/></svg>Tel: (+351) 912 408 733</li>
      <li><svg width="18" height="18" viewBox="0 0 24 24" fill="none" stroke="#fff" stroke-width="1.6"><rect x="3" y="5" width="18" height="14" rx="1"/><path d="M3 6l9 7 9-7"/></svg>E: info@peter-lindqvist.net</li>
      <li><svg width="18" height="18" viewBox="0 0 24 24" fill="none" stroke="#fff" stroke-width="1.6"><path d="M12 22s7-7 7-12a7 7 0 0 0-14 0c0 5 7 12 7 12z"/><circle cx="12" cy="10" r="2.5"/></svg>Rua das Amoreiras 112B<br>Bairro Alto Verde<br>Lisbon 1250-024</li>
    </ul>
  </div>
  <div class="abs foot-col" style="left:921px">
    <h4>Socials</h4>
    <ul><li><span class="social-mark"></span>Socialbook</li><li><span class="social-mark"></span>Snapgram</li></ul>
  </div>
  <div class="abs copyright">© 2025 Peter Joseph Lindqvist</div>
</footer>

</body>
</html>
```